Event Graphic for Free Community Event

We need a graphic created for a community event that is aimed at families with younger children called Totz Jam. This is a free event and has a fair/carnival feel to it with rides, games, and food. I need the graphic to be flexible enough to be able to be modified and used in a variety of ways on different print and digital marketing materials. I also need the centerpiece of the design to be an event logo that can be used as a standalone element.

The overall feel needs to be fun and friendly with a slightly modern edge to it. Attached are some images used in past events. These are for reference only and do not need to be simulated or used in the final product.

Target Market(s)

Families with children

Industry/Entity Type

Church

Font styles to use
Sans Serif

Requirements
Must have
• - Logo that incorporates the event name
- Event Date: September 19 2020
- Event Time: 10am - 2pm
- Church name and logo incorporated: Bright Harbor Community Church (see attached logo files)
Nice to have
• - Bright colors
- Flexible design elements that are interchangeable and scalable for use of the design in different layouts across different mediums and materials.
Should not have
• - Any references or images related to drugs, alcohol, tobacco, or other subjects that would be inappropriate for children.

```html
<!DOCTYPE html>
<html lang="en">
<head>
<meta charset="utf-8">
<title>Totz Jam – Event Flyer</title>
<link rel="stylesheet" href="https://fonts.googleapis.com/css2?family=Luckiest+Guy&family=Anton&family=Fredoka:wght@600;700&family=Poppins:wght@800&display=swap">
<style>
  :root {
    --sun-yellow: #fdb813;
    --sun-light: #ffd75a;
    --sun-pale: #fff3c4;
    --teal: #1d6b6b;
    --teal-pale: #eaf4f2;
    --title-red: #e2312c;
    --orange: #f47a20;
    --navy: #14306b;
    --panel-grey: #e9e4dc;
    --decor-tone: #7fb6a8;
    --white: #ffffff;
    --ink: #1c1c1c;
  }
  * { margin: 0; padding: 0; box-sizing: border-box; }
  html, body { width: 678px; height: 1200px; overflow: hidden; }
  body { background: var(--white); }

  .flyer {
    position: relative;
    width: 678px;
    height: 1200px;
    overflow: hidden;
    background: radial-gradient(circle at 50% 55%, var(--sun-pale) 0%, var(--sun-light) 35%, var(--sun-yellow) 75%);
  }

  .bunting {
    position: absolute; left: 0; top: 0; width: 678px; height: 70px;
    background: linear-gradient(90deg, #e2312c, #f4c21f, #2a9bd7, #7ac143, #e2312c, #f4c21f, #2a9bd7);
    opacity: .55;
    clip-path: polygon(0 0, 100% 0, 100% 40%, 0 70%);
  }

  .title-panel { position: absolute; left: 0; top: 0; }

  .photo {
    position: absolute;
    border-radius: 50%;
    border: 5px solid var(--white);
    box-shadow: 0 3px 8px rgba(0,0,0,.25);
  }
  .photo--swing  { left: 12px;  top: 150px; width: 150px; height: 150px; background: linear-gradient(160deg, #8fb8d8, #46683f); }
  .photo--slide  { left: 22px;  top: 330px; width: 145px; height: 145px; background: linear-gradient(160deg, #6e9a4f, #e8632b 60%, #2f77c4); }
  .photo--climb  { right: 12px; top: 130px; width: 148px; height: 148px; background: linear-gradient(160deg, #dcdcd8, #a9b3bb); }
  .photo--table  { right: 22px; top: 305px; width: 140px; height: 140px; background: linear-gradient(160deg, #f1eee8, #c7b39a); }
  .photo--bungee { left: 257px; top: 440px; width: 164px; height: 164px; background: linear-gradient(180deg, #8cc6f0, #2f7fc9); }

  .decor-spot {
    position: absolute; top: 30px; width: 54px; height: 80px;
    border-radius: 40%;
    background: var(--decor-tone);
    z-index: 2;
  }
  .decor-spot--left  { left: 118px; }
  .decor-spot--right { right: 118px; }

  .event-logo { margin: 0; }
  .event-logo__line {
    position: absolute; left: 0; width: 678px; text-align: center; display: block;
  }
  .event-logo__top {
    top: 118px;
    font-family: "Luckiest Guy", system-ui, sans-serif;
    font-size: 112px; line-height: 1;
    color: var(--title-red);
    letter-spacing: 4px;
    text-shadow: 3px 3px 0 var(--white), -3px -3px 0 var(--white), 3px -3px 0 var(--white), -3px 3px 0 var(--white), 5px 7px 6px rgba(0,0,0,.3);
  }
  .event-logo__bottom {
    top: 225px;
    font-family: "Anton", Impact, sans-serif;
    font-size: 200px; line-height: 1;
    color: var(--teal);
    letter-spacing: 6px;
    text-shadow: 4px 4px 0 var(--white), -4px -4px 0 var(--white), 4px -4px 0 var(--white), -4px 4px 0 var(--white), 6px 8px 8px rgba(0,0,0,.3);
  }

  .date-band {
    position: absolute; left: 90px; top: 618px; width: 498px; height: 118px;
    background: var(--white);
    clip-path: polygon(2% 8%, 20% 0, 60% 6%, 98% 2%, 100% 40%, 97% 92%, 70% 100%, 30% 94%, 0 100%, 3% 55%);
    opacity: .95;
  }
  .event-date, .event-time {
    position: absolute; left: 0; width: 678px; text-align: center;
    font-family: "Fredoka", system-ui, sans-serif; font-weight: 700;
  }
  .event-date { top: 626px; font-size: 44px; line-height: 1.1; color: var(--teal); letter-spacing: 1px; }
  .event-time {
    top: 682px; font-size: 40px; line-height: 1.1; color: var(--teal-pale);
    text-shadow: 2px 2px 0 var(--teal), -2px -2px 0 var(--teal), 2px -2px 0 var(--teal), -2px 2px 0 var(--teal);
  }

  .activities {
    position: absolute; left: 0; top: 780px; width: 678px; text-align: center;
    font-family: "Fredoka", system-ui, sans-serif; font-weight: 700; color: var(--teal);
  }
  .activities__heading { font-size: 40px; line-height: 1.1; font-weight: 700; margin-bottom: 18px; }
  .activities__list { list-style: none; font-size: 32px; line-height: 1.3; font-weight: 600; }
  .activities__list span { white-space: nowrap; margin: 0 6px; }
  .activities__list span::before {
    content: ""; display: inline-block; width: 14px; height: 14px; border-radius: 50%;
    background: var(--orange); margin-right: 8px; vertical-align: 5px;
  }

  .contact {
    position: absolute; top: 980px; left: 120px; height: 46px; display: flex;
    font-family: "Anton", Impact, sans-serif; font-size: 28px; line-height: 1.4; letter-spacing: 1px;
  }
  .contact__label {
    background: var(--orange); color: var(--white); padding: 2px 36px 0 28px;
    clip-path: polygon(0 0, 100% 0, 90% 100%, 0 100%, 5% 50%);
  }
  .contact__phone {
    background: var(--navy); color: var(--white); padding: 3px 34px 0 40px; margin-left: -14px;
    clip-path: polygon(7% 0, 100% 0, 100% 100%, 0 100%);
    font-size: 26px;
  }

  .footer {
    position: absolute; left: 0; bottom: 0; width: 678px; height: 150px;
    background: linear-gradient(180deg, rgba(255,255,255,0) 0%, var(--white) 30%);
  }
  .footer__church {
    position: absolute; left: 40px; top: 70px;
    font-family: "Poppins", system-ui, sans-serif; font-weight: 800;
    font-size: 26px; line-height: 1.2; color: var(--navy);
  }
  .footer__mark {
    position: absolute; right: 36px; top: 56px; width: 62px; height: 62px;
    border-radius: 50%; background: var(--ink);
  }
</style>
</head>
<body>
<main class="flyer">
  <div class="bunting" role="img" aria-label="Colourful bunting flags and confetti"></div>

  <svg class="title-panel" width="678" height="620" viewBox="0 0 678 620" aria-hidden="true">
    <polygon points="339,40 560,150 560,480 339,590 118,480 118,150" fill="var(--panel-grey)" stroke="var(--white)" stroke-width="6"/>
  </svg>

  <div class="decor-spot decor-spot--left" role="img" aria-label="Hanging paper lantern decoration"></div>
  <div class="decor-spot decor-spot--right" role="img" aria-label="Hanging paper lantern decoration"></div>

  <div class="photo photo--swing" role="img" aria-label="Photo of children on a swing ride"></div>
  <div class="photo photo--slide" role="img" aria-label="Photo of an inflatable slide"></div>
  <div class="photo photo--climb" role="img" aria-label="Photo of children on a climbing wall"></div>
  <div class="photo photo--table" role="img" aria-label="Photo of children eating at a table"></div>

  <h1 class="event-logo">
    <span class="event-logo__line event-logo__top">TOTZ</span>
    <span class="event-logo__line event-logo__bottom">JAM</span>
  </h1>

  <div class="photo photo--bungee" role="img" aria-label="Photo of a child on a bungee trampoline"></div>

  <div class="date-band" aria-hidden="true"></div>
  <p class="event-date">SEPTEMBER 19 2020</p>
  <p class="event-time">10AM - 2PM</p>

  <section class="activities">
    <h2 class="activities__heading">FUN ACTIVITIES</h2>
    <ul class="activities__list">
      <li><span>FOOD</span><span>BUNGEE JUMP</span><span>ROCK WALL</span></li>
      <li><span>RIDES</span><span>INFLATABLES</span></li>
    </ul>
  </section>

  <div class="contact">
    <span class="contact__label">CALL US</span>
    <span class="contact__phone">1-555-014-3030</span>
  </div>

  <footer class="footer">
    <p class="footer__church">BRIGHT HARBOR COMMUNITY CHURCH</p>
    <div class="footer__mark" aria-hidden="true"></div>
  </footer>
</main>
</body>
</html>
```